Miss Dorrel Teen Postcard for special events

Need creative display for platform of logo for Miss Dorrel on her large postcards. Be kind, be bold, be brave, be you is the message. Please include this quote:
Kindness is the language which the deaf can hear
and the blind can see. - Hobart Lune
Her title is 2017 Miss Dorrel Hollin Starlet Teen. Her name is Corinne Vask. We have pics that we want included on the card. We want it to have a front and back. You can use any combination of the photos. thanks!

Target Market(s)

Youth/ Young Adults

Industry/Entity Type

Events

Font styles to use
Sans Serif
Script

Colors
86cfc6
33b8a4
3276b5
0255a3

Requirements
Must have
• Kindness is the language which the deaf can hear
• and the blind can see. - Hobart Lune
• Title-
• Name
• She is partial to the jumpsuit photo for the front but open to others
• Be Kind, Be Bold, Be Brave, Be you - would like this on the front
• Also please include Instgram: crvask202 twitter: crvask202 corinne47@pelvomail.net
• #kindboldbrave
Nice to have
• Anything that would inspire youth especially. Have begun events at hospitals and lining up work to assist with donations for community resources but not sure that is appropriate for this. We lean more towards the green than the blue, unless it ties with other things you see better- or a better shade.thanks
Should not have
• Should be age appropriate and appropriate for all ages.
• Postcard is for handing out / does not need to be mailed. Can seek revisions if this becomes the case

```html
<!DOCTYPE html>
<html lang="en">
<head>
<meta charset="utf-8">
<title>Miss Dorrel Teen Postcard</title>
<link rel="stylesheet" href="https://fonts.googleapis.com/css2?family=Anton&family=Comfortaa:wght@700&display=swap">
<style>
  :root{
    --stage:#2a2a2a;
    --card:#ffffff;
    --band-grey:#555657;
    --band-grey-dark:#3f4041;
    --teal:#22b59f;
    --sky:#8fd8f4;
    --ink:#4a4b4c;
    --stamp:#9a9b9d;
    --rule:#8a8a8a;
    --photo-warm:#c9a58a;
    --photo-green:#6f8f5a;
    --photo-gold:#e9b53c;
    --photo-pink:#e7c2b8;
  }
  *{box-sizing:border-box;margin:0;padding:0}
  html,body{width:1200px;height:800px;overflow:hidden;background:var(--stage)}
  .canvas{position:relative;width:1200px;height:800px}
  .postcard{position:absolute;top:210px;width:570px;height:380px;background:var(--card);overflow:hidden}
  .postcard--front{left:20px}
  .postcard--back{left:610px}

  .photo{position:absolute}
  .photo--sash{left:232px;top:100px;width:86px;height:226px;background:linear-gradient(180deg,var(--photo-green),var(--photo-pink))}
  .photo--portrait{left:322px;top:60px;width:248px;height:266px;background:linear-gradient(160deg,var(--photo-green) 0%,var(--photo-warm) 55%,#d9b79e 100%)}
  .photo--street{left:0;top:0;width:170px;height:150px;background:linear-gradient(150deg,#9aa38c,var(--photo-warm))}
  .photo--gold{left:174px;top:0;width:110px;height:150px;background:linear-gradient(180deg,var(--photo-gold),#c98f5e)}

  .quote-band{position:absolute;left:0;top:0;width:570px;height:150px}
  .quote{position:absolute;left:40px;top:18px;width:470px;text-align:center;color:#fff;
    font-family:"Comfortaa",sans-serif;font-size:16px;line-height:1.45}

  .title{position:absolute;left:22px;top:140px;width:205px;font-family:"Anton",sans-serif;text-align:center}
  .title__year{display:block;color:var(--teal);font-size:84px;line-height:1}
  .title__name{display:block;color:var(--ink);font-size:37px;line-height:1.05;margin-top:4px}
  .title__program{display:block;color:var(--teal);font-size:20px;line-height:1.15}
  .title__person{display:block;color:var(--ink);font-size:23px;line-height:1.15}

  .contact-band{position:absolute;left:0;bottom:0;width:100%;height:52px;background:var(--sky);border-top:4px solid var(--teal);
    display:flex;align-items:center;gap:18px;padding:0 20px;font-family:"Comfortaa",sans-serif;font-size:14px;color:var(--ink)}
  .contact{display:flex;align-items:center;gap:7px}
  .contact__mark{width:16px;height:16px;background:var(--ink);border-radius:2px}
  .contact-band--back{justify-content:flex-end;padding-right:26px}

  .stamp{position:absolute;right:40px;top:28px;width:62px;height:62px;background:var(--stamp)}
  .address-lines{position:absolute;left:300px;top:200px;width:240px}
  .address-lines span{display:block;height:1px;background:var(--rule);margin-bottom:34px}
</style>
</head>
<body>
<main class="canvas">

  <section class="postcard postcard--front" aria-label="Postcard front">
    <div class="photo photo--sash" role="img" aria-label="Photo of Corinne Vask wearing her crown and sash"></div>
    <div class="photo photo--portrait" role="img" aria-label="Portrait photo of Corinne Vask outdoors"></div>

    <svg class="quote-band" viewBox="0 0 570 150" aria-hidden="true">
      <defs>
        <linearGradient id="bandShade" x1="0" y1="0" x2="0" y2="1">
          <stop offset="0" stop-color="#5d5e5f"/>
          <stop offset="1" stop-color="#414243"/>
        </linearGradient>
      </defs>
      <path d="M0 0H570V62C420 96 250 120 0 136Z" fill="url(#bandShade)"/>
      <path d="M0 141C250 125 420 101 570 67" fill="none" stroke="#22b59f" stroke-width="4"/>
    </svg>
    <p class="quote">Kindness Is The Language Which The Deaf<br>Can Hear And The Blind Can See<br>- Hobart Lune</p>

    <h1 class="title">
      <span class="title__year">2017</span>
      <span class="title__name">Miss Dorrel</span>
      <span class="title__program">Hollin Starlet Teen.</span>
      <span class="title__person">“Corinne Vask”</span>
    </h1>

    <footer class="contact-band">
      <span class="contact"><span class="contact__mark"></span>crvask202</span>
      <span class="contact"><span class="contact__mark"></span>crvask202</span>
      <span class="contact"><span class="contact__mark"></span>corinne47@pelvomail.net</span>
    </footer>
  </section>

  <section class="postcard postcard--back" aria-label="Postcard back">
    <div class="photo photo--street" role="img" aria-label="Photo of Corinne Vask in a city street"></div>
    <div class="photo photo--gold" role="img" aria-label="Photo of Corinne Vask on a gold background"></div>
    <div class="stamp"></div>
    <div class="address-lines"><span></span><span></span><span></span></div>
    <footer class="contact-band contact-band--back">
      <span class="contact">corinne47@pelvomail.net</span>
    </footer>
  </section>

</main>
</body>
</html>
```